I need the following on my business card:
- Name: Dana Whitcomb
- License # 0M93216
- Title: Producer
- Phone: (555) 017-3904
- Email: Dana@CorbelInsuranceServices.com

- Company: Corbel Insurance Services
- Address: 27408 Larkmoor Ave Suite 610, Fernbrook Vale, ST 90217
- Website: www.CorbelInsuranceServices.com

Also add our slogan on the card: "Where Care Meets Confidence"

```html
<!DOCTYPE html>
<html lang="en">
<head>
<meta charset="utf-8">
<title>Corbel Insurance Services – Business Card</title>
<link href="https://fonts.googleapis.com/css2?family=Montserrat:wght@400;500;600;700&display=swap" rel="stylesheet">
<style>
  :root {
    --bg: #d3d4d6;
    --green: #008a37;
    --navy: #2a2366;
    --white: #ffffff;
  }
  * { margin: 0; padding: 0; box-sizing: border-box; }
  html, body { width: 900px; height: 1200px; overflow: hidden; }
  body {
    background: var(--bg);
    font-family: "Montserrat", sans-serif;
    position: relative;
  }
  .card {
    position: absolute;
    left: 135px;
    width: 631px;
    height: 357px;
    border-radius: 11px;
    overflow: hidden;
  }
  .card--front {
    top: 215px;
    background: var(--green);
    color: var(--white);
    text-align: center;
  }
  .front-brand {
    position: absolute;
    top: 168px;
    left: 0; right: 0;
    font-size: 36px;
    font-weight: 600;
    letter-spacing: 0.5px;
    line-height: 1;
  }
  .front-slogan {
    position: absolute;
    top: 264px;
    left: 0; right: 0;
    font-size: 16px;
    font-weight: 600;
    letter-spacing: 1.2px;
    text-transform: uppercase;
  }
  .card--back {
    top: 629px;
    background: var(--white);
    color: var(--navy);
  }
  .person { position: absolute; left: 36px; top: 75px; }
  .person-name { font-size: 24px; font-weight: 700; color: var(--green); line-height: 1.2; }
  .person-title { font-size: 15px; font-weight: 500; margin-top: 2px; }
  .back-brand {
    position: absolute;
    right: 42px;
    top: 80px;
    font-size: 20px;
    font-weight: 700;
    color: var(--navy);
  }
  .address {
    position: absolute;
    left: 36px;
    top: 181px;
    font-size: 15px;
    font-weight: 500;
    font-style: normal;
    line-height: 23px;
  }
  .contacts {
    position: absolute;
    left: 36px;
    top: 245px;
    list-style: none;
    font-size: 15px;
    font-weight: 500;
    line-height: 23px;
  }
  .contacts li { display: flex; align-items: center; gap: 6px; }
  .contacts svg { width: 12px; height: 12px; flex: none; }
  .contacts .phone { letter-spacing: 3px; }
  .contacts .web { letter-spacing: 0.9px; }
  .band { position: absolute; left: 0; top: 313px; width: 631px; height: 44px; }
  .license {
    position: absolute;
    left: 409px;
    top: 320px;
    font-size: 16px;
    font-weight: 700;
    letter-spacing: 1.2px;
    color: var(--white);
  }
</style>
</head>
<body>
  <section class="card card--front">
    <div class="front-brand">Corbel Insurance Services</div>
    <p class="front-slogan">Where Care Meets Confidence</p>
  </section>

  <section class="card card--back">
    <div class="person">
      <h1 class="person-name">Dana Whitcomb</h1>
      <p class="person-title">Producer</p>
    </div>
    <div class="back-brand">Corbel Insurance Services</div>
    <address class="address">
      27408 Larkmoor Ave Suite 610,<br>Fernbrook Vale, ST 90217
    </address>
    <ul class="contacts">
      <li class="phone">
        <svg viewBox="0 0 24 24" fill="var(--green)"><path d="M6.6 10.8a15.1 15.1 0 0 0 6.6 6.6l2.2-2.2c.3-.3.7-.4 1-.2 1.1.4 2.3.6 3.6.6.6 0 1 .4 1 1V20c0 .6-.4 1-1 1A17 17 0 0 1 3 4c0-.6.4-1 1-1h3.5c.6 0 1 .4 1 1 0 1.3.2 2.5.6 3.6.1.3 0 .7-.2 1z"/></svg>
        (555) 017-3904
      </li>
      <li>
        <svg viewBox="0 0 24 24" fill="var(--green)"><path d="M2 5h20v2l-10 7L2 7z M2 9l6 4.5L2 18z M22 9v9l-6-4.5z M9.5 14.6 12 16.4l2.5-1.8L22 19H2z"/></svg>
        Dana@CorbelInsuranceServices.com
      </li>
      <li class="web">
        <svg viewBox="0 0 24 24"><circle cx="12" cy="12" r="9.5" fill="none" stroke="var(--green)" stroke-width="2"/><path d="M2.5 12h19M12 2.5c3 3 3 16 0 19M12 2.5c-3 3-3 16 0 19" fill="none" stroke="var(--green)" stroke-width="1.6"/></svg>
        www.CorbelInsuranceServices.com
      </li>
    </ul>
    <svg class="band" viewBox="0 0 631 44" aria-hidden="true">
      <path d="M0 19 H387 L403 3 H631 V44 H0 Z" fill="var(--green)"/>
      <path d="M0 18 H386 L402 2 H631" fill="none" stroke="var(--navy)" stroke-width="2.5"/>
    </svg>
    <p class="license">License # 0M93216</p>
  </section>
</body>
</html>
```